Vallée douce coffee - Label design

Watchout: Keep in mind while you submit it needs to be a LABEL (that will be sticked on brown kraft 250 g side gusset coffee pouches). No custom pack for time being (need more scale to custom print pack).

Looking for a label design for my new Beau Matin collection of freshly roasted, single origin specialty coffee. Brand name is Vallée Douce (it means red earth and alludes to the soil coffee grows on at high altitude in Africa. It also alludes to the red color of the coffee fruit). Brand selling line is "Pure Origin Coffee". Label to go as stickers on 250 g side gusset coffee pouches in Kraft brown paper (will print labels and stick on packs, packs are 80 mm wide and 260 mm long). This is a relatively complex project comprising the "vallée douce" brand logo (funded separately, winner will have the job), the "Beau Matin" collection visual identity, iconic assets for brand and collection recognition across lineup, educational visual icons, text placeholders. It needs to combine hard point visual elements and soft points (text placeholder) which I can easily edit on need basis (text needs to be "outlines" for easy editing after submission). Winner of label submission gets to design brand logo. I will ultimately need 3 different labels for our Beau Matin collection, one for each continent our coffee comes from (Africa, Asia, Latin America). This pitch should focus on the Africa one only. Winner will then have opportunity to design the other ones in consistent way.

BRIEF:
We roast single origin, high quality specialty coffee from high altitude estates in Africa (volcanic slopes in Congo and Burundi, Highlands in Ethiopia and Kenya) Design need to induce the premiumness of the proposition (this is a collection called "Beau Matin"), as well the the unique geographical origins of our coffee (without being too specific as we want to use same label for all our African origins) -oversized shape of continent in background + some visuals conveying the African roots could work well. It needs to create a mental Journey "back to the origins" - of mankind, of unique terroirs creating the best coffee, of our unspoilt roots. So the Journey themes is critical (to be expressed by the telegram type of font, by the way Africa is brought to life,etc.). At the same time keep in mind label space is limited (label stickers go on 250 g coffee pouches made in kraft brown paper) and we want to have a pure design, which leaves room to the text placeholder (see below) and is easily recognizable and reapplicable across the SKUs (we will add Asia and Latin America packs once we lock Africa). As such we need to strike right balance between visual differentiation by origin (Africa, Asia, Latin America) and common iconic assets for brand recognition and lineup harmonization (same font, same way the continent is brought to life, same structure of the label, differentiation by color background,etc.).

We need placeholder for text that will specify exact name of estate, county of origin, coffee type, roasting level and tasting notes. Here I will allow myself some creative direction: it should be in the format of a vintage luggage tag (see attached examples) where we can edit content in Telegram font (our coffee sourcing changes often). We will need to assess if the tag remains standard across collection, or whether we are able to give it a visual twist for each origin (Africa, Asia, Latin America). That would be nicer (see Moonpeak "Ledgers" example), but priority of the text placeholder is clarity of information above anything else.

Last nice to have (if it time allows) we need educational visual icons (ideally as separate small round labels we can stick on the pack above the main label) for recommended brewing method (filter, espresso, italian moka, french press).

Reason: Still looking for the design in line with brief. Will send feedback to the top 3 routes today.

Target Market(s)

Switzerland

Industry/Entity Type

Coffee Shop

Logo Text

Vallée douce -Pure Origin Coffee

Font styles to use
Other font styles liked:
• TELEGRAM type of font to induce geographical journey, single origin,.. For the "luggage tag" placeholder

Requirements
Must have
• - Brand name: Vallée Douce. Brand selling line: Pure Origin Coffee. Brand Logo: winner of label submission gets to design brand logo
• - Collection name: BEAU MATIN (written, I can see well as a vertical block). name of SKU: AFRICA (visualized a must, written tbc).
• - Text place holder (vintage luggage tag in telegram font) : we will show there name of estate, country of origin, tasting notes. I could see nicely a baggage tag format, where we fill in the details in telegram type of font.
• - 100% single origin Arabica (at the bottom)
• - 250 g (at the bottom)
• Technical Specs:
• A. Artwork must be supplied in either Adobe illustrator or Adobe Photoshop files or Coral Draw files
• B. Create all text in artwork in ‘ outlines ’
• C. The resolution of photographic image files must be no less than 350 dpi
• D. Never flatten the file as we require all layers
• E. All Photoshop image files should be linked and attached. Never flatten the layers and do not change the directory
• F. Create the images with CMYK colour mode ( RGB colour mode is not for printing)
• G. If you are going to use a spot colour please reference the Pantone ( PMS #)
• H. Designate all ‘Transparent’ areas in the artwork with a custom Pantone colour as well as designating the layer’s name as ‘ Transparent’. Please indicate specifically which pantone colour is designated for the ‘transparent’ area.
• I. Reduce any barcodes to 85% as a minimum scale
Nice to have
• - educational simple visual icons on recommended brewing method (filer, italian moka, french press or espresso) as additional small stickers to stick above main label

```html
<!DOCTYPE html>
<html lang="en">
<head>
<meta charset="utf-8">
<title>Vallée Douce – Beau Matin Collection Label</title>
<link href="https://fonts.googleapis.com/css2?family=Oswald:wght@300;400&family=Playfair+Display:wght@700;900&family=Lobster+Two:ital,wght@1,700&family=Special+Elite&family=Courier+Prime&display=swap" rel="stylesheet">
<style>
  :root {
    --backdrop: #e8e6e2;
    --kraft: #b58c63;
    --kraft-shade: #a9805a;
    --ink-dark: #3a2a1e;
    --rust: #9a3c22;
    --rust-deep: #8b3219;
    --cream: #fbe8cb;
    --cream-light: #fdf0dc;
    --ochre: #f3bf77;
    --tag-paper: #d2a777;
    --grommet: #8a97a4;
  }
  * { box-sizing: border-box; margin: 0; padding: 0; }
  html, body { width: 1012px; height: 1200px; overflow: hidden; background: var(--backdrop); }
  .canvas { position: relative; width: 1012px; height: 1200px; }

  .label {
    position: absolute; left: 108px; top: 100px; width: 520px; height: 995px;
    background: var(--kraft);
    box-shadow: 0 4px 14px rgba(0,0,0,.18);
  }

  .brew-badge {
    position: absolute; left: 31px; top: 123px; width: 92px; height: 92px;
    border-radius: 50%; background: var(--cream-light);
    border: 2px solid var(--rust);
    display: flex; flex-direction: column; align-items: center; justify-content: center;
  }
  .brew-badge svg { width: 40px; height: 34px; margin-top: -4px; }
  .brew-badge__name {
    font-family: "Lobster Two", cursive; font-style: italic; font-weight: 700;
    font-size: 16px; color: var(--ink-dark); margin-top: 2px;
  }

  .collection { position: absolute; left: 160px; top: 132px; color: var(--rust); }
  .collection__name {
    font-family: "Oswald", sans-serif; font-weight: 300; font-size: 46px;
    letter-spacing: 3px; line-height: 1;
  }
  .collection__word {
    font-family: "Oswald", sans-serif; font-weight: 300; font-size: 17px;
    letter-spacing: 6.4px; line-height: 1; margin-top: 6px; margin-left: 2px;
  }

  .brand { position: absolute; left: 0; right: 0; top: 310px; text-align: center; color: var(--ink-dark); }
  .brand__name {
    font-family: "Playfair Display", serif; font-weight: 900; font-size: 58px;
    letter-spacing: 1px; line-height: 1; transform: scaleX(.9);
  }
  .brand__line {
    font-family: "Playfair Display", serif; font-weight: 700; font-size: 28px;
    letter-spacing: 4px; line-height: 1; margin-top: 14px;
  }

  .panel {
    position: absolute; left: 39px; top: 475px; width: 433px; height: 453px;
    border: 2px solid var(--rust); padding: 4px; background: var(--kraft);
  }
  .panel__inner {
    position: relative; width: 100%; height: 100%;
    background: linear-gradient(160deg, var(--cream-light), var(--cream));
  }
  .panel__claim {
    position: absolute; left: 24px; top: 52px;
    font-family: "Lobster Two", cursive; font-style: italic; font-weight: 700;
    font-size: 28px; line-height: 1.32; color: var(--rust);
  }
  .panel__ribbon {
    position: absolute; left: 287px; top: -2px; width: 97px; height: 164px;
    background: var(--ink-dark); border-radius: 0 0 8px 8px;
    border: 2px solid var(--rust); border-top: none;
    display: flex; align-items: flex-end; justify-content: center; padding-bottom: 14px;
  }
  .brand-seal {
    width: 88px; height: 88px; border-radius: 50%; background: var(--cream-light);
    display: flex; align-items: center; justify-content: center;
    font-family: "Special Elite", monospace; font-size: 13px; color: var(--rust); text-align: center;
  }
  .panel__pattern {
    position: absolute; left: 0; right: 0; top: 214px; height: 186px;
    background: linear-gradient(180deg, var(--ochre), #f6cb8c);
  }
  .panel__footer {
    position: absolute; left: 0; right: 0; bottom: 0; height: 38px;
    background: var(--rust-deep);
    display: flex; align-items: center; justify-content: flex-end; padding-right: 32px;
    font-family: "Courier Prime", monospace; font-size: 21px; color: var(--cream-light); letter-spacing: 1px;
  }

  .tag-string { position: absolute; left: 0; top: 0; width: 1012px; height: 1200px; pointer-events: none; }

  .luggage-tag {
    position: absolute; left: 692px; top: 218px; width: 250px; height: 130px;
    transform: rotate(20deg); transform-origin: 20px 65px;
  }
  .luggage-tag svg { position: absolute; inset: 0; }
  .luggage-tag__text {
    position: absolute; left: 56px; top: 14px; width: 180px; text-align: center; color: var(--rust);
  }
  .luggage-tag__kicker {
    font-family: "Lobster Two", cursive; font-style: italic; font-weight: 700;
    font-size: 15px; color: var(--ink-dark); border-bottom: 2px solid var(--rust); padding-bottom: 3px;
  }
  .luggage-tag__name {
    font-family: "Special Elite", monospace; font-size: 27px; line-height: 1.15;
    border-bottom: 2px solid var(--rust); padding: 3px 0 2px;
  }
  .luggage-tag__line {
    font-family: "Special Elite", monospace; font-size: 13px; color: var(--ink-dark);
    letter-spacing: 1.5px; margin-top: 4px;
  }
</style>
</head>
<body>
<div class="canvas">

  <div class="label">
    <div class="brew-badge">
      <svg viewBox="0 0 40 34" aria-hidden="true">
        <path d="M15 2c-2 3 2 4 0 7M21 2c-2 3 2 4 0 7" fill="none" stroke="#3a2a1e" stroke-width="1.6" stroke-linecap="round"/>
        <path d="M6 13h24v7a9 9 0 0 1-9 9h-6a9 9 0 0 1-9-9z" fill="#3a2a1e"/>
        <path d="M30 15h3a3.5 3.5 0 0 1 0 7h-3" fill="none" stroke="#3a2a1e" stroke-width="2"/>
        <rect x="2" y="30" width="34" height="2.4" rx="1.2" fill="#3a2a1e"/>
      </svg>
      <span class="brew-badge__name">espresso</span>
    </div>

    <div class="collection">
      <div class="collection__name">BEAU MATIN</div>
      <div class="collection__word">COLLECTION</div>
    </div>

    <div class="brand">
      <div class="brand__name">VALLÉE DOUCE</div>
      <div class="brand__line">PURE ORIGIN COFFEE</div>
    </div>

    <div class="panel">
      <div class="panel__inner" role="img" aria-label="Faint oversized map of the African continent in the background">
        <div class="panel__claim">100% Single<br>Origin Arabica</div>
        <div class="panel__ribbon">
          <div class="brand-seal">Vallée<br>Douce</div>
        </div>
        <div class="panel__pattern" role="img" aria-label="Decorative African tribal pattern band in ochre tones"></div>
        <div class="panel__footer">250 g</div>
      </div>
    </div>
  </div>

  <svg class="tag-string" viewBox="0 0 1012 1200" aria-hidden="true">
    <path d="M712 238 C 650 200, 560 150, 515 155 C 495 160, 505 185, 540 195 C 600 212, 670 228, 712 238"
          fill="none" stroke="#b8743f" stroke-width="2.2"/>
  </svg>

  <div class="luggage-tag">
    <svg viewBox="0 0 250 130" aria-hidden="true">
      <path d="M38 0H250V130H38L0 96V34Z" fill="var(--tag-paper)"/>
      <circle cx="22" cy="65" r="13" fill="#9a3c22"/>
      <circle cx="22" cy="65" r="8" fill="var(--grommet)"/>
      <circle cx="22" cy="65" r="4.5" fill="#e8e6e2"/>
    </svg>
    <div class="luggage-tag__text">
      <div class="luggage-tag__kicker">Geographical Journey</div>
      <div class="luggage-tag__name">Vallée Douce</div>
      <div class="luggage-tag__line">Pure Origin Coffee</div>
    </div>
  </div>

</div>
</body>
</html>
```